custom carpentry, woodworking and home repair company needs logo design and business card design

Attention: I apologize but I just received notification from my state that I cannot use the company name that I originally submitted (Beyond The Bench). The new name will be Joinolux We need a company logo and business card design for our new company based in the Hampton Roads area of Virginia. The company name is Joinolux. The final design should give a first impression of true craftsmanship and attention to detail. We would like the card to include the company name, my name Mark Tellman (owner), phone number (757) 348-2615, website (joinolux-example.com) and email address (mark@joinolux-example.com). Everything else is up to your discretion. Thanks, have fun, and good luck.

Industry/Entity Type

Business

Contact Information for Business Card

See project description

Logo Text

see project description

Colors

Designer to choose colors to be used in the design.

```html
<!DOCTYPE html>
<html lang="en">
<head>
<meta charset="utf-8">
<title>Joinolux Business Card</title>
<link href="https://fonts.googleapis.com/css2?family=Open+Sans:wght@400;600;800&display=swap" rel="stylesheet">
<style>
  :root {
    --backdrop: #1f1f21;
    --wood-dark: #3b1d0c;
    --wood-mid: #6a3416;
    --wood-light: #8a4a22;
    --green: #1f7a3a;
    --green-light: #3fae4d;
    --ink-green: #14532a;
    --gold: #f0c64a;
    --paper: #ffffff;
  }
  * { box-sizing: border-box; margin: 0; padding: 0; }
  html, body { width: 1200px; height: 1200px; overflow: hidden; }
  body {
    background: var(--backdrop);
    font-family: "Open Sans", Arial, sans-serif;
    position: relative;
  }
  .card {
    position: absolute;
    left: 180px;
    width: 840px;
    height: 480px;
    overflow: hidden;
    box-shadow: 0 14px 30px rgba(0,0,0,.55);
  }
  .card--front { top: 90px; }
  .card--back { top: 630px; background: var(--paper); }

  .wood {
    position: absolute;
    background: linear-gradient(100deg, var(--wood-dark) 0%, var(--wood-mid) 30%, var(--wood-light) 50%, var(--wood-mid) 70%, var(--wood-dark) 100%);
  }
  .card--front .wood { inset: 0; }

  .brand {
    position: absolute;
    left: 0; right: 0;
    text-align: center;
    font-weight: 800;
    letter-spacing: 3px;
    text-transform: uppercase;
  }
  .brand__mark {
    display: inline-block;
    width: 34px; height: 34px;
    border-radius: 50%;
    vertical-align: middle;
    margin-right: 16px;
    position: relative; top: -6px;
  }
  .brand__tagline {
    position: absolute;
    left: 0; right: 0;
    text-align: center;
    font-weight: 600;
    font-size: 15px;
    letter-spacing: 2px;
    text-transform: uppercase;
  }
  .rule {
    position: absolute;
    height: 3px;
  }

  /* front */
  .card--front .brand { top: 160px; font-size: 66px; color: var(--paper); }
  .card--front .brand__mark { background: var(--paper); }
  .card--front .brand__tagline { top: 255px; color: var(--paper); }
  .card--front .rule { background: var(--paper); left: 170px; right: 170px; }
  .card--front .rule--top { top: 145px; }
  .card--front .rule--bottom { top: 290px; }
  .front__web {
    position: absolute;
    left: 0; right: 0; top: 360px;
    text-align: center;
    color: var(--paper);
    font-weight: 800;
    font-size: 22px;
    letter-spacing: 1.5px;
  }

  /* back */
  .card--back .brand { top: 110px; font-size: 66px; color: var(--ink-green); }
  .card--back .brand__mark { background: var(--green); }
  .card--back .brand__tagline { top: 205px; color: var(--green-light); }
  .card--back .rule { background: var(--green); left: 170px; right: 170px; }
  .card--back .rule--top { top: 95px; }
  .card--back .rule--bottom { top: 240px; }
  .card--back .band-line {
    position: absolute; left: 0; right: 0; top: 272px;
    height: 8px; background: var(--green);
  }
  .card--back .wood { left: 0; right: 0; top: 280px; height: 170px; }

  .owner {
    position: absolute;
    left: 100px; top: 318px;
    width: 260px;
    text-align: right;
    padding-right: 30px;
    border-right: 2px solid rgba(255,255,255,.8);
    height: 100px;
  }
  .owner__name { color: var(--paper); font-weight: 800; font-size: 30px; line-height: 1.2; }
  .owner__role { color: var(--gold); font-weight: 800; font-size: 22px; }

  .contact {
    position: absolute;
    left: 390px; top: 318px;
    list-style: none;
  }
  .contact__item {
    display: flex; align-items: center;
    color: var(--paper);
    font-size: 23px;
    line-height: 1;
    height: 34px;
    margin-bottom: 2px;
  }
  .contact__icon {
    width: 26px; height: 26px;
    background: var(--gold);
    margin-right: 16px;
    flex: none;
  }
</style>
</head>
<body>

<section class="card card--front">
  <div class="wood" role="img" aria-label="Dark walnut wood grain texture"></div>
  <div class="rule rule--top"></div>
  <div class="brand"><span class="brand__mark"></span>Joinolux</div>
  <div class="brand__tagline">Carpentry, Woodworking and Home Repair</div>
  <div class="rule rule--bottom"></div>
  <div class="front__web">WWW.JOINOLUX-EXAMPLE.COM</div>
</section>

<section class="card card--back">
  <div class="rule rule--top"></div>
  <div class="brand"><span class="brand__mark"></span>Joinolux</div>
  <div class="brand__tagline">Carpentry, Woodworking and Home Repair</div>
  <div class="rule rule--bottom"></div>
  <div class="band-line"></div>
  <div class="wood" role="img" aria-label="Dark walnut wood grain texture"></div>

  <div class="owner">
    <div class="owner__name">MARK TELLMAN</div>
    <div class="owner__role">OWNER</div>
  </div>

  <ul class="contact">
    <li class="contact__item">
      <svg class="contact__icon" viewBox="0 0 26 26" aria-hidden="true">
        <path d="M8 6 L11 6 L12 10 L10 11.5 Q12 15 14.5 16 L16 14 L20 15 L20 18 Q15 20 10.5 15.5 Q6 11 8 6 Z" fill="#3b1d0c"/>
      </svg>
      (757) 348-2615
    </li>
    <li class="contact__item">
      <svg class="contact__icon" viewBox="0 0 26 26" aria-hidden="true">
        <rect x="5" y="8" width="16" height="11" fill="none" stroke="#3b1d0c" stroke-width="1.8"/>
        <path d="M5 8 L13 14 L21 8" fill="none" stroke="#3b1d0c" stroke-width="1.8"/>
      </svg>
      mark@joinolux-example.com
    </li>
    <li class="contact__item">
      <svg class="contact__icon" viewBox="0 0 26 26" aria-hidden="true">
        <circle cx="13" cy="13" r="8" fill="none" stroke="#3b1d0c" stroke-width="1.6"/>
        <ellipse cx="13" cy="13" rx="3.5" ry="8" fill="none" stroke="#3b1d0c" stroke-width="1.4"/>
        <line x1="5" y1="13" x2="21" y2="13" stroke="#3b1d0c" stroke-width="1.4"/>
      </svg>
      joinolux-example.com
    </li>
  </ul>
</section>

</body>
</html>
```